Box design for velomcrate

VelomCrate ackage design development brief.
Technical specification:
Package measurements – 200x200x40mm or 150x150x60mm (see pictures of an example below).
Design only for outer layer, no printing inside.
As the box itself is the main product, the aim of this design is to be outstanding – modern, clean,
sophisticated, attractive, memorable and providing WoW-effect to the consumer.

Industry/Entity Type

Printing

```html
<!DOCTYPE html>
<html lang="en">
<head>
<meta charset="utf-8">
<title>VelomCrate Box Design</title>
<link rel="stylesheet" href="https://fonts.googleapis.com/css2?family=Arimo:wght@400&display=swap">
<style>
  :root {
    --paper: #ffffff;
    --dieline: #5a5a5a;
    --panel: #f9ecee;
    --band: #f7d6da;
    --ink: #4a4a4a;
    --brand-grey: #8c8c8c;
    --accent: #a3475f;
    --dusty-rose: #c98f9a;
    --blush: #f2b8bf;
  }
  html, body {
    margin: 0;
    padding: 0;
    width: 1200px;
    height: 1029px;
    overflow: hidden;
    background: var(--paper);
  }
  .canvas {
    position: relative;
    width: 1200px;
    height: 1029px;
    font-family: "Arimo", Arial, sans-serif;
  }
  .dieline {
    position: absolute;
    inset: 0;
  }
  .lid-panel {
    position: absolute;
    left: 193px;
    top: 22px;
    width: 813px;
    height: 813px;
    background: var(--panel);
  }
  .hero-decoration {
    position: absolute;
    left: 9px;
    top: 24px;
    width: 795px;
    height: 767px;
    background:
      radial-gradient(circle at 50% 48%, #ffffff 0%, rgba(255,255,255,0) 18%),
      radial-gradient(ellipse at 50% 50%, #e3c3c8 0%, var(--dusty-rose) 45%, rgba(201,143,154,0) 72%);
    opacity: 0.75;
  }
  .product-name {
    position: absolute;
    left: 16px;
    top: 14px;
    margin: 0;
    font-size: 35px;
    font-weight: 400;
    color: var(--ink);
    line-height: 1.2;
  }
  .product-subtitle {
    position: absolute;
    left: 16px;
    top: 63px;
    margin: 0;
    font-size: 27px;
    color: var(--ink);
    line-height: 1.2;
  }
  .tagline {
    position: absolute;
    left: 16px;
    top: 727px;
    margin: 0;
    font-size: 26px;
    color: var(--ink);
    line-height: 33px;
  }
  .brand-name {
    position: absolute;
    right: 24px;
    top: 756px;
    margin: 0;
    font-size: 30px;
    font-weight: 400;
    letter-spacing: 2px;
    color: var(--brand-grey);
  }
  .brand-square {
    position: absolute;
    right: 98px;
    top: 690px;
    width: 44px;
    height: 44px;
    background: var(--accent);
    opacity: 0.8;
  }
  .flap-band {
    position: absolute;
    left: 193px;
    top: 878px;
    width: 813px;
    height: 127px;
    background: var(--band);
    display: flex;
    align-items: center;
    justify-content: center;
  }
  .flap-text {
    margin: 0;
    font-size: 30px;
    color: var(--accent);
  }
</style>
</head>
<body>
  <div class="canvas">
    <svg class="dieline" width="1200" height="1029" viewBox="0 0 1200 1029" aria-hidden="true">
      <g fill="none" stroke="var(--dieline)" stroke-width="1">
        <rect x="0.5" y="0.5" width="1199" height="855.5"/>
        <line x1="171.5" y1="0" x2="171.5" y2="1028.5"/>
        <line x1="1029.5" y1="0" x2="1029.5" y2="1028.5"/>
        <line x1="171.5" y1="1028.5" x2="1029.5" y2="1028.5"/>
      </g>
    </svg>

    <section class="lid-panel">
      <div class="hero-decoration" role="img" aria-label="Large brand symbol decoration in dusty rose and blush pink with a soft white glow at its centre"></div>
      <h1 class="product-name">Product Name</h1>
      <p class="product-subtitle">Your Text Here</p>
      <p class="tagline">Tagline or anything<br>you need to mention</p>
      <div class="brand-square" aria-hidden="true"></div>
      <p class="brand-name">VELOMCRATE</p>
    </section>

    <section class="flap-band">
      <p class="flap-text">Your Text Here or Tagline Product Information</p>
    </section>
  </div>
</body>
</html>
```